Biotech company website design

We are looking for innovative design of our upcoming website. We are a small biotechnology company in Europe dealing with life science products and services.
Updates

Please incorporate the following top level links:
ABOUT US, PRODUCTS, SERVICES, SUPPLIERS, NEWS AND PROMOS, CONTACT US

Target Market(s)

Science people, hospitals, universities ....

Industry/Entity Type

It Company

Requirements
Must have
• Must incorporate our current logo (its color toning)

```html
<!DOCTYPE html>
<html lang="en">
<head>
<meta charset="utf-8">
<title>Verdant BioSystems</title>
<link rel="stylesheet" href="https://fonts.googleapis.com/css2?family=Arimo:ital,wght@0,400;0,700;1,700&family=PT+Sans:wght@400;700&display=swap">
<style>
:root{
  --green:#4a9e2b;
  --green-dark:#2f7a1a;
  --green-light:#5aab3e;
  --green-text:#4fa12a;
  --lime:#9ccc2c;
  --page:#ebe8e2;
  --white:#ffffff;
  --ink:#222222;
  --body:#555555;
  --muted:#666666;
  --blue:#1a86c4;
}
*{margin:0;padding:0;box-sizing:border-box}
html,body{width:942px;height:1200px;overflow:hidden}
body{position:relative;background:var(--page);font-family:"Arimo",Arial,sans-serif;color:var(--ink)}
.abs{position:absolute}
.backdrop{left:0;top:0;width:942px;height:378px;background:linear-gradient(90deg,#8a6f6a 0%,#c9a7a0 8%,#d8dce0 30%,#c8ccd2 60%,#e1c35a 88%,#caa636 100%)}
.backdrop-fade{left:0;top:330px;width:942px;height:50px;background:linear-gradient(180deg,rgba(235,232,226,0),var(--page))}
.topbar{left:75px;top:0;width:786px;height:50px;background:var(--green);border-top:3px solid var(--green-dark)}
.home-icon{left:10px;top:10px}
.main-nav{right:19px;top:19px;display:flex;gap:14px;list-style:none}
.main-nav li{color:var(--white);font-weight:700;font-size:10.5px;letter-spacing:.1px}
.brandbar{left:75px;top:62px;width:786px;height:46px;background:var(--white)}
.brand{left:10px;top:8px;display:flex;align-items:center;gap:8px}
.brand-mark{width:22px;height:22px;background:var(--lime)}
.brand-name{font-family:"PT Sans",sans-serif;font-size:20px;color:#222}
.social-dots{right:16px;top:16px;display:flex;gap:2px}
.social-dots span{width:19px;height:19px;border-radius:50%}
.hero{left:76px;top:108px;width:785px;height:332px;background:radial-gradient(ellipse at 70% 40%,#ddd8d4 0%,#b7bcc4 45%,#8e98a6 100%);box-shadow:0 6px 10px rgba(0,0,0,.25)}
.hero-caption{left:76px;top:174px;width:314px;height:104px;background:rgba(80,80,80,.7);padding:13px 24px;font-family:"PT Sans",sans-serif;font-size:19.5px;line-height:23px;color:var(--white)}
.slider-arrows{left:810px;top:315px;display:flex;gap:2px}
.slider-arrows span{width:14px;height:15px;background:rgba(120,120,120,.8);color:#fff;font-size:10px;line-height:15px;text-align:center}
.section-title{left:0;top:466px;width:934px;text-align:center;font-size:12.5px;letter-spacing:.3px;color:#111}
.card{top:494px;width:216px;height:242px;background:var(--white);box-shadow:0 3px 6px rgba(0,0,0,.15);overflow:hidden}
.card-photo{height:128px}
.card h3{font-size:9.5px;font-weight:700;margin:12px 0 0 18px;color:#111}
.card p{font-size:10.5px;line-height:15px;color:var(--body);margin:7px 14px 0 20px}
.card-more{right:0;bottom:0}
.welcome{left:116px;top:751px;width:694px;height:180px;background:var(--white);box-shadow:0 4px 6px rgba(0,0,0,.12)}
.welcome h2{position:absolute;left:13px;top:10px;font-size:12px;font-weight:700;color:#333}
.welcome h2 em{font-style:normal;color:var(--green-text)}
.welcome .intro{position:absolute;left:15px;top:33px;width:420px;font-size:8.8px;line-height:13px;color:#333}
.welcome .highlight{position:absolute;left:16px;top:102px;width:430px;font-size:11.5px;line-height:14px;font-weight:700;font-style:italic;color:var(--green-text)}
.welcome .divider{position:absolute;left:475px;top:22px;width:1px;height:110px;background:#ddd}
.news{position:absolute;left:498px;top:10px;width:180px}
.news h2{position:relative;left:0;top:0;font-size:12px;color:#444}
.news-item{margin-top:7px;font-size:8.8px;line-height:13px;color:#333}
.news-item time{display:block;color:var(--green-text);font-style:italic;margin-bottom:3px;margin-left:2px}
.news-item p{margin-left:1px}
.footer{left:0;top:963px;width:942px;height:237px;background:var(--green);border-top:2px solid var(--green-dark);overflow:hidden}
.footer-curve{left:0;top:0}
.footer h4{position:absolute;font-size:10.5px;font-weight:700;color:var(--white)}
.footer-nav{position:absolute;left:119px;top:39px;list-style:none}
.footer-nav li{font-size:9.5px;line-height:15.8px;font-weight:700;color:var(--white)}
.field{position:absolute;left:231px;width:152px;height:29px;background:var(--white);border:1px solid #bbb;font-size:10.5px;color:#999;padding:7px 7px}
.subscribe-btn{position:absolute;left:231px;top:112px;width:82px;height:23px;background:linear-gradient(#8cd98a,#4fb354);border:1px solid #3a9a40;color:var(--white);font-size:8px;font-weight:700;line-height:21px;padding-left:10px}
.social-list{position:absolute;left:455px;top:44px;list-style:none}
.social-list li{display:flex;align-items:center;gap:10px;height:23px;font-family:"PT Sans",sans-serif;font-size:11.5px;color:var(--white)}
.social-list span{width:20px;height:20px;border-radius:3px}
.footer-brand{left:618px;top:77px;width:184px;height:31px;background:var(--white);display:flex;align-items:center;gap:8px;padding-left:6px}
.footer-brand .brand-mark{width:20px;height:20px}
.footer-brand .brand-name{font-size:17px}
.legal{right:140px;top:150px;text-align:right;font-size:9.5px;line-height:12px;color:#d9ecd0}
</style>
</head>
<body>
<div class="abs backdrop" role="img" aria-label="Blurred colourful laboratory background"></div>
<div class="abs backdrop-fade"></div>

<header class="abs topbar">
  <svg class="abs home-icon" width="18" height="18" viewBox="0 0 18 18"><path d="M9 1 1 8.5h2.5V17h4.2v-5h2.6v5h4.2V8.5H17z" fill="#fff"/></svg>
  <ul class="abs main-nav">
    <li>ABOUT US</li><li>PRODUCTS</li><li>SERVICES</li><li>SUPPLIERS</li><li>NEWS AND PROMOS</li><li>CONTACT US</li>
  </ul>
</header>

<div class="abs brandbar">
  <div class="abs brand"><span class="brand-mark"></span><span class="brand-name">Verdant BioSystems</span></div>
  <div class="abs social-dots">
    <span style="background:#e8761c"></span><span style="background:#d2382a"></span><span style="background:#3b5b99"></span><span style="background:#2ba6de"></span>
  </div>
</div>

<div class="abs hero" role="img" aria-label="Lab scientist in protective goggles and mask holding a syringe filter"></div>
<div class="abs hero-caption">Verdant strives to provide a high standard of healthcare and improve people’s life</div>
<div class="abs slider-arrows"><span>‹</span><span>›</span></div>

<h2 class="abs section-title">OUR PRODUCTS</h2>

<article class="abs card" style="left:113px">
  <div class="card-photo" role="img" aria-label="Researcher pipetting samples in a laboratory" style="background:linear-gradient(90deg,#c9787c,#7fa8c8 50%,#e6eef4)"></div>
  <h3>Sed ut persde omnis iste natus</h3>
  <p>Lorem ipsum dolor sit amet, consectet uer scing elit, sed diam nonummy nibh dolor sit amet, consectetuer scing elit, sed diam nonummy nibh</p>
  <svg class="abs card-more" width="21" height="21" viewBox="0 0 21 21"><path d="M21 0V21H0z" fill="#1a86c4"/><path d="M13 14h6M16 11v6" stroke="#fff" stroke-width="1.6"/></svg>
</article>
<article class="abs card" style="left:360px">
  <div class="card-photo" role="img" aria-label="Molecule model, flask and microscope in blue tones" style="background:linear-gradient(135deg,#2c4aa8,#9bb0e0 50%,#dfe6f6)"></div>
  <h3>Sed ut persde omnis iste natus</h3>
  <p>Lorem ipsum dolor sit amet, consectet uer scing elit, sed diam nonummy nibh dolor sit amet, consectetuer scing elit, sed diam nonummy nibh</p>
  <svg class="abs card-more" width="21" height="21" viewBox="0 0 21 21"><path d="M21 0V21H0z" fill="#1a86c4"/><path d="M13 14h6M16 11v6" stroke="#fff" stroke-width="1.6"/></svg>
</article>
<article class="abs card" style="left:595px">
  <div class="card-photo" role="img" aria-label="Scientist looking into a microscope" style="background:linear-gradient(90deg,#e8e4de,#cfc9c2 50%,#eef0ec)"></div>
  <h3>Sed ut persde omnis iste natus</h3>
  <p>Lorem ipsum dolor sit amet, consectet uer scing elit, sed diam nonummy nibh dolor sit amet, consectetuer scing elit, sed diam nonummy nibh</p>
  <svg class="abs card-more" width="21" height="21" viewBox="0 0 21 21"><path d="M21 0V21H0z" fill="#1a86c4"/><path d="M13 14h6M16 11v6" stroke="#fff" stroke-width="1.6"/></svg>
</article>

<section class="abs welcome">
  <h2>WELCOME TO <em>VERDANT BIO SYSTEMS</em></h2>
  <p class="intro">Sed ut perspiciatis unde omnis iste natus error sit voluptatem accusantium doloremque laudantium totam rem eaque ipsa quae ab illo inventore veritatis et quasi architecto beatae vitae dicta sunt explicabo. Nemo enim ip voluptatem quia voluptas sit aspernatur aut odit aut fugit, sed quia conse quuntur magni dolores eos qui ration voluptatem sequi nesciunt.</p>
  <p class="highlight">Sed ut perspiciatis unde omnis iste natus error sit voluptatem accusantiu doloremque laudantium</p>
  <div class="divider"></div>
  <div class="news">
    <h2>COMPANY NEWS</h2>
    <div class="news-item"><time>Dec 2010</time><p>Sed ut perspiciatis unde omnis iste natus voluptatem accusantium doloremque<br>Read more..</p></div>
    <div class="news-item"><time>Oct 2013</time><p>Sed ut perspiciatis unde omnis iste natus voluptatem accusantium doloremque<br>Read more..</p></div>
  </div>
</section>

<footer class="abs footer">
  <svg class="abs footer-curve" width="942" height="237" viewBox="0 0 942 237"><path d="M0 237C180 110 500 20 942 -5V237z" fill="#5aab3e"/></svg>
  <h4 style="left:119px;top:16px">NAVIGATION</h4>
  <ul class="footer-nav">
    <li>About us</li><li>Products</li><li>Services</li><li>Suppliers</li><li>News And Promos</li><li>Contact Us</li>
  </ul>
  <h4 style="left:230px;top:14px">SUBSCRIBE TO OUR NEWSLETTER</h4>
  <div class="field" style="top:36px">Name</div>
  <div class="field" style="top:71px">Email</div>
  <div class="subscribe-btn">SUBSCRIBE</div>
  <h4 style="left:457px;top:17px">GET CONNECTED</h4>
  <ul class="social-list">
    <li><span style="background:#3b5b99"></span>Friendbook</li>
    <li><span style="background:#2ba6de"></span>Chirper</li>
    <li><span style="background:#d2382a"></span>Circles Plus</li>
    <li><span style="background:#c4302b"></span>Clipstream.tv/Lumo</li>
  </ul>
  <div class="abs footer-brand"><span class="brand-mark"></span><span class="brand-name">Verdant BioSystems</span></div>
  <div class="abs legal">Copyright 2013. All rights reserved<br>Terms &amp; Conditions &nbsp;- &nbsp;&nbsp;Privacy &nbsp;&nbsp;- &nbsp;&nbsp;Disclaimer</div>
</footer>
</body>
</html>
```